Very clean, very simple business card needed.

I am looking for a VERY simple business card. I have attached our logo. I would like it to be a mainly white card. I have picked double sided but would be open to single as well. I want the overall feel to be simple, classic, and professional. Thank you.

Industry/Entity Type

Consultant

Contact Information for Business Card

Dennis Pellowe

862 North Larchmere Avenue, Summit Floor, Cedarholt, Wisconsin 60719
denny@hollisterbaycapital.example
www.hollisterbaycapital.example

Font styles to use
Serif

Colors

Designer to choose colors to be used in the design.

Requirements
Must have
• The business card details and in an editable form to change the names and emails of employees easily.
Nice to have
• n/a
Should not have
• Pictures, big lines and stripes, too much color.

```html
<!DOCTYPE html>
<html lang="en">
<head>
<meta charset="utf-8">
<title>Hollister Bay Capital — Business Card</title>
<link rel="stylesheet" href="https://fonts.googleapis.com/css2?family=Raleway:wght@400;500&display=swap">
<style>
  :root {
    --backdrop: #d9d9d7;
    --card: #f7f7f5;
    --ink: #2c4a6c;
    --ink-soft: #3c5878;
    --mark: #2f4f73;
  }
  * { box-sizing: border-box; margin: 0; padding: 0; }
  html, body {
    width: 1200px;
    height: 720px;
    overflow: hidden;
  }
  body {
    background: var(--backdrop);
    display: flex;
    align-items: center;
    justify-content: center;
    font-family: "Raleway", "Helvetica Neue", Arial, sans-serif;
    color: var(--ink);
  }
  .card {
    position: relative;
    width: 980px;
    height: 560px;
    background: var(--card);
    border-radius: 4px;
    box-shadow: 0 2px 6px rgba(0,0,0,0.08);
  }
  .brand {
    position: absolute;
    top: 92px;
    right: 96px;
    display: flex;
    flex-direction: column;
    align-items: flex-end;
    gap: 22px;
  }
  .brand-square {
    width: 150px;
    height: 58px;
    background: var(--mark);
    margin-right: 150px;
  }
  .brand-name {
    font-weight: 400;
    font-size: 38px;
    letter-spacing: 0.04em;
    text-transform: uppercase;
    color: var(--ink);
    line-height: 1;
  }
  .contact {
    position: absolute;
    left: 96px;
    bottom: 86px;
  }
  .contact-name {
    font-weight: 500;
    font-size: 31px;
    color: var(--ink);
    margin-bottom: 16px;
  }
  .contact-list {
    list-style: none;
    font-size: 23px;
    color: var(--ink-soft);
    line-height: 1.4;
  }
  .contact-item {
    display: flex;
    align-items: flex-start;
    gap: 12px;
  }
  .contact-icon {
    flex: 0 0 22px;
    width: 22px;
    height: 22px;
    margin-top: 6px;
    fill: none;
    stroke: var(--ink);
    stroke-width: 1.8;
  }
  .contact-icon.solid { fill: var(--ink); stroke: none; }
</style>
</head>
<body>
  <main class="card">
    <header class="brand">
      <div class="brand-square"></div>
      <div class="brand-name">Hollister Bay Capital</div>
    </header>

    <section class="contact">
      <h1 class="contact-name">Dennis Pellowe</h1>
      <ul class="contact-list">
        <li class="contact-item">
          <svg class="contact-icon solid" viewBox="0 0 24 24" aria-hidden="true">
            <path d="M12 1.5a7.5 7.5 0 0 0-7.5 7.5c0 5.6 7.5 13.5 7.5 13.5s7.5-7.9 7.5-13.5A7.5 7.5 0 0 0 12 1.5zm0 10.5a3 3 0 1 1 0-6 3 3 0 0 1 0 6z"/>
          </svg>
          <span>862 North Larchmere Avenue, Summit Floor,<br>Cedarholt, Wisconsin 60719</span>
        </li>
        <li class="contact-item">
          <svg class="contact-icon" viewBox="0 0 24 24" aria-hidden="true">
            <rect x="2" y="5" width="20" height="14" rx="1"/>
            <path d="M2 5l10 8 10-8M2 19l7-7M22 19l-7-7"/>
          </svg>
          <span>denny@hollisterbaycapital.example</span>
        </li>
        <li class="contact-item">
          <svg class="contact-icon" viewBox="0 0 24 24" aria-hidden="true">
            <circle cx="12" cy="12" r="10"/>
            <ellipse cx="12" cy="12" rx="4.5" ry="10"/>
            <path d="M2 12h20M4 6.5h16M4 17.5h16"/>
          </svg>
          <span>www.hollisterbaycapital.example</span>
        </li>
      </ul>
    </section>
  </main>
</body>
</html>
```